Business Card Design for the Larkmoor Venous and Larkmoor Aesthetic Institute Clinics

We need one business card design for an existing company based in Chicago called Larkmoor Venous Institute and Larkmoor Aesthetic Institute. We are vein and plastic surgery clinics. There are two speared logos for each company Larkmoor Venous and Larkmoor Aesthetic Institute.Before we had two separate busniess cards for each company, but now we want to combained them into one, and thus the both logos need to be on the the card. I would like to see the design that follow the design of our brochure and folders. The colors included need to be the ones of our two logos(orange, gray and teal--> see the attachment). The design needs to represent two companies under one roof. The final design should communicate trust and loyalty

Target Market(s)

Medical

Industry/Entity Type

Medical

Contact Information for Business Card

Larkmoor Venous InstituteLarkmoor Aesthetic Institute4817 W. Dunmore Ridge Rd. Chicago, IL 60618www.larkmoorvenous-example.comwww.larkmooraesthetic-example.comTelephone (773) 555-0182Fax (773) 555-0183

Requirements
Must have
• Both logos, ultimately representing both companies at one card

```html
<!DOCTYPE html>
<html lang="en">
<head>
<meta charset="utf-8">
<title>Larkmoor Venous &amp; Larkmoor Aesthetic Institute – Business Card</title>
<link rel="stylesheet" href="https://fonts.googleapis.com/css2?family=Questrial&display=swap">
<style>
  :root {
    --backdrop: #4a4a4a;
    --card: #efeff0;
    --ink-gray: #6d6e70;
    --logo-gray: #a7a8aa;
    --teal: #0e8a92;
    --orange: #f0813a;
    --bridge: #3f2f28;
    --ink-dark: #2b2b2b;
  }
  * { box-sizing: border-box; margin: 0; padding: 0; }
  html, body { width: 1200px; height: 900px; overflow: hidden; }
  body {
    background: var(--backdrop);
    font-family: "Questrial", "Century Gothic", sans-serif;
    position: relative;
  }
  .card {
    position: absolute;
    left: 320px;
    width: 560px;
    height: 320px;
    background: var(--card);
    box-shadow: 0 10px 30px rgba(0,0,0,.35);
  }
  .card--back { top: 90px; }
  .card--front { top: 490px; }

  /* Back side */
  .contact-bar {
    position: absolute;
    left: 70px; top: 130px;
    width: 430px; height: 14px;
    background: linear-gradient(90deg, var(--teal) 0%, var(--bridge) 55%, var(--orange) 100%);
  }
  .contact {
    position: absolute;
    left: 76px; top: 156px;
    color: var(--ink-gray);
    font-size: 19px;
    line-height: 1.3;
    letter-spacing: .3px;
  }
  .contact__phones { padding-left: 40px; display: flex; gap: 34px; }

  /* Front side */
  .brand-bar {
    position: absolute;
    right: 48px; top: 34px;
    width: 14px; height: 252px;
    background: linear-gradient(180deg, var(--orange) 0%, var(--bridge) 50%, var(--teal) 100%);
  }
  .clinic {
    position: absolute;
    right: 84px;
    text-align: right;
  }
  .clinic--venous { top: 62px; }
  .clinic--aesthetic { top: 178px; }
  .clinic__name {
    display: flex;
    align-items: center;
    justify-content: flex-end;
    gap: 12px;
    font-size: 24px;
    letter-spacing: .5px;
    text-transform: uppercase;
  }
  .clinic__dot { width: 16px; height: 16px; border-radius: 50%; flex: none; }
  .clinic--venous .clinic__name { color: var(--teal); }
  .clinic--venous .clinic__dot { background: var(--teal); }
  .clinic--aesthetic .clinic__name { color: var(--orange); }
  .clinic--aesthetic .clinic__dot { background: var(--orange); }
  .clinic__web {
    margin-top: 8px;
    font-size: 13px;
    color: var(--ink-dark);
    letter-spacing: .2px;
  }
</style>
</head>
<body>
  <section class="card card--back" aria-label="Business card, contact side">
    <div class="contact-bar"></div>
    <div class="contact">
      <p class="contact__address">4817 W. Dunmore Ridge Rd. Chicago, IL 60618</p>
      <p class="contact__phones"><span>T: (773) 555-0182</span><span>F: (773) 555-0183</span></p>
    </div>
  </section>

  <section class="card card--front" aria-label="Business card, brand side">
    <div class="clinic clinic--venous">
      <p class="clinic__name"><span class="clinic__dot"></span>Larkmoor Venous Institute</p>
      <p class="clinic__web">www.larkmoorvenous-example.com</p>
    </div>
    <div class="clinic clinic--aesthetic">
      <p class="clinic__name"><span class="clinic__dot"></span>Larkmoor Aesthetic Institute</p>
      <p class="clinic__web">www.larkmooraesthetic-example.com</p>
    </div>
    <div class="brand-bar"></div>
  </section>
</body>
</html>
```